Calm Fern Wellcare- Aged Care and Community Services

Looking for brochure to advertise our services. I will attach a draft that we do not want to use. Looking for graphics that are as natural as possible to present a personalised service. We supply services to aged people and people with disability. Please make it look classy and professional at the same time. I am looking for creativity. I have also attached the logo. Site addresses can be the last page. ideally looking for 2 designs, one A4 and another smaller possibly DL. Looking for creative out of the box thinkers. Thank you.

Target Market(s)

Aged Care service providers, disability service providers and private hospitals

Font styles to use
Serif
Sans Serif
Script

Colors
6b449b
886aae
eea4c8
f59195
fac994
3176b5
0555a3
cedeed
e4daeb

Requirements
Must have
• Targeted imagery, content and contact details
Nice to have
• personal profiles of people happy with our services

```html
<!DOCTYPE html>
<html lang="en">
<head>
<meta charset="utf-8">
<title>Calm Fern Wellcare – Brochure Pages</title>
<link href="https://fonts.googleapis.com/css2?family=Satisfy&family=Questrial&display=swap" rel="stylesheet">
<style>
  :root{
    --purple:#6b449b;
    --purple-mid:#886aae;
    --pink:#eea4c8;
    --lilac:#e4daeb;
    --ink:#3a3340;
    --bg:#8a8a8a;
    --white:#ffffff;
  }
  *{box-sizing:border-box;margin:0;padding:0}
  html,body{width:1200px;height:1200px;overflow:hidden}
  body{background:var(--bg);font-family:"Questrial",sans-serif;color:var(--ink);position:relative}
  .page{position:absolute;width:386px;height:542px;background:var(--white);overflow:hidden}
  .page--cover{left:186px;top:31px}
  .page--philosophy{left:636px;top:31px}
  .page--services{left:186px;top:618px}
  .page--contact{left:636px;top:618px}
  .waves{position:absolute;left:0;top:0;width:386px;height:542px}
  .photo{position:absolute}
  .brand{position:absolute;display:flex;align-items:center;gap:6px;font-family:"Questrial",sans-serif;font-size:15px;color:var(--white);letter-spacing:.3px}
  .brand__dot{width:11px;height:11px;border-radius:50%;background:var(--white)}
  .brand--purple{color:var(--purple)}
  .brand--purple .brand__dot{background:var(--purple)}
  .script{font-family:"Satisfy",cursive;color:var(--purple);font-weight:400}
  .cover__title{position:absolute;left:0;width:100%;top:402px;text-align:center;font-size:33px}
  .cover__lede{position:absolute;left:30px;width:326px;top:455px;text-align:center;font-size:11.6px;line-height:1.4}
  .cover__rule{position:absolute;left:148px;width:90px;top:506px;border-top:1px solid #999}
  .cover__url{position:absolute;left:0;width:100%;top:518px;text-align:center;font-size:10px;color:var(--purple)}
  .section-title{position:absolute;font-size:15px}
  .copy{position:absolute;font-size:7.2px;line-height:1.27;text-align:justify}
  .copy p+p{margin-top:7px}
  .url-foot{position:absolute;font-size:7.6px;color:var(--white)}
  .bullets{position:absolute;list-style:none;font-size:7.2px;line-height:1.27}
  .bullets li{position:relative;padding-left:13px;margin-bottom:3.6px}
  .bullets li::before{content:"";position:absolute;left:2px;top:2px;width:5px;height:5px;border-radius:50%;background:var(--purple-mid)}
  .lead-in{position:absolute;font-size:7.4px;color:var(--purple);font-weight:700}
  .contact{position:absolute;left:212px;top:446px;color:var(--white)}
  .contact__title{font-family:"Satisfy",cursive;font-size:16px;border-bottom:1px solid var(--pink);display:inline-block;padding-bottom:2px;margin-bottom:5px}
  .contact__row{display:flex;align-items:center;gap:6px;font-size:7.3px;margin-top:3px}
  .contact__row--phone{font-size:11px;margin-bottom:3px}
  .contact__row svg{flex:none}
</style>
</head>
<body>

<!-- Cover -->
<section class="page page--cover">
  <div class="photo" role="img" aria-label="Smiling elderly woman seated beside a young nurse in a white uniform in a sunny garden" style="left:0;top:0;width:386px;height:420px;background:linear-gradient(135deg,#c9b25e,#8e9a4a 40%,#d9c9b8 70%,#e8e0d6)"></div>
  <svg class="waves" viewBox="0 0 386 542" aria-hidden="true">
    <defs>
      <linearGradient id="g1" x1="0" x2="1"><stop offset="0" stop-color="#6b449b"/><stop offset="1" stop-color="#886aae"/></linearGradient>
    </defs>
    <path d="M0 0H386V48C320 40 280 80 230 110C180 140 110 120 60 110C35 106 15 112 0 120Z" fill="url(#g1)"/>
    <path d="M0 110C15 104 35 100 60 104C110 114 180 134 230 104C280 74 320 36 386 42V50C320 46 282 84 232 114C182 144 110 126 60 116C35 112 15 116 0 122Z" fill="#fff"/>
    <path d="M0 380C90 410 200 340 290 310C330 298 360 298 386 302V542H0Z" fill="#eea4c8"/>
    <path d="M0 392C90 420 200 360 290 332C330 320 360 318 386 322V542H0Z" fill="url(#g1)"/>
    <path d="M0 405C70 420 160 382 250 372C320 364 360 380 386 392V542H0Z" fill="#fff"/>
  </svg>
  <div class="brand" style="left:28px;top:62px"><span class="brand__dot"></span>Calm Fern Wellcare</div>
  <h1 class="cover__title script">Reimaging Healthcare</h1>
  <p class="cover__lede">Calm Fern Wellcare is a staffing provider with a contemporary approach to recruiting and placing exceptional people in human services.</p>
  <div class="cover__rule"></div>
  <p class="cover__url">www.calmfernwellcare.com.au</p>
</section>

<!-- Philosophy -->
<section class="page page--philosophy">
  <div class="photo" role="img" aria-label="Elderly residents playing cards around an outdoor table with a carer" style="left:0;top:0;width:386px;height:240px;background:linear-gradient(160deg,#4f7a3a,#7fa35a 45%,#c9a98a 75%,#9a7b66)"></div>
  <svg class="waves" viewBox="0 0 386 542" aria-hidden="true">
    <defs>
      <linearGradient id="g2" x1="0" x2="1"><stop offset="0" stop-color="#6b449b"/><stop offset="1" stop-color="#886aae"/></linearGradient>
    </defs>
    <path d="M0 205C80 240 170 200 260 188C320 180 360 190 386 200V280C360 250 320 230 260 232C180 236 90 262 0 222Z" fill="#eea4c8"/>
    <path d="M0 212C90 250 180 218 260 214C320 211 360 228 386 246V542H0Z" fill="#fff"/>
    <path d="M0 500C110 520 230 470 386 478V542H0Z" fill="url(#g2)"/>
    <path d="M0 494C110 514 230 462 386 470V476C230 468 110 520 0 500Z" fill="#eea4c8"/>
  </svg>
  <h2 class="section-title script" style="left:18px;top:235px">Our Philosophy</h2>
  <div class="copy" style="left:18px;top:258px;width:350px">
    <p>Calm Fern Wellcare has a client focused approach which ensures it identifies individual client requirements to facilitate for a unique partnership without ambiguity. Our approach focuses on key pain areas of our clients which go beyond staffing needs. We ensure we look at the profile of the clients in your care to identify similar values and develop a “team based” system to ensure you always receive the same staff that meet your needs when you book your shifts.</p>
    <p>Our staff retention programs focus on the key drivers for staff to perform the work they do and whether their values are aligned to supporting vulnerable groups in society. With a proactive reward and recognition program, Calm Fern are well informed of areas of improvement to retain the very best talent. We believe our staff are a pillar to what we do, which is why we take every step to ensure they feel part of the great achievement and reward brought by supporting people who need assistance.</p>
  </div>
  <h2 class="section-title script" style="left:18px;top:387px">Why Clients Choose Us</h2>
  <div class="copy" style="left:18px;top:411px;width:350px">
    <p>Calm Fern Wellcare partners with likeminded organisations with a passion for making a difference to the lives of the vulnerable. We have differentiated ourselves by redefining the model of traditional staffing agencies and developed an obsessive desire to meet our clients needs. We genuinely care about what we do and know the impact under resourcing can do to day to day service delivery and overall quality outcomes.</p>
    <p>If you partner with us, we guarantee a tailored approach to meeting your needs.</p>
  </div>
  <p class="url-foot" style="right:22px;top:518px">www.calmfernwellcare.com.au</p>
</section>

<!-- Services -->
<section class="page page--services">
  <div class="photo" role="img" aria-label="Carer with her hand on the shoulder of a smiling elderly man in a wheelchair" style="left:170px;top:260px;width:216px;height:250px;background:radial-gradient(circle at 60% 50%,#c9a48a,#e8dcd6 55%,#ffffff 80%)"></div>
  <svg class="waves" viewBox="0 0 386 542" aria-hidden="true">
    <defs>
      <linearGradient id="g3" x1="0" x2="1"><stop offset="0" stop-color="#6b449b"/><stop offset="1" stop-color="#886aae"/></linearGradient>
    </defs>
    <path d="M0 504C110 526 240 480 386 490V542H0Z" fill="url(#g3)"/>
    <path d="M0 496C110 518 240 470 386 482V488C240 476 110 524 0 502Z" fill="#eea4c8"/>
  </svg>
  <h2 class="section-title script" style="left:19px;top:24px">Our Value Proposition</h2>
  <ul class="bullets" style="left:19px;top:50px;width:345px">
    <li>Our people are individually selected and participate in robust recruitment processes</li>
    <li>We treat everyone with respect and believe our staff are the purpose of our existence</li>
    <li>We are responsive to our clients priorities and walk along their journey to achieving operational excellence</li>
    <li>We believe in ethical practices, transparency, and accountability</li>
    <li>We are deliberate in our approach and have a passion for human services</li>
    <li>We have a ‘bias for action’ and unceasingly pursue opportunities to change and adapt</li>
    <li>to the needs of our clients and environment</li>
  </ul>
  <h2 class="section-title script" style="left:19px;top:174px">Services</h2>
  <div class="copy" style="left:19px;top:200px;width:345px">
    <p>Our mission is to supply values driven, responsive, conscientious, and responsible personnel to the aged care sector, disability services, private and public health sectors. Our passion for human services and experience in recruitment, enables us to attract exceptional people with great values ready and willing to make a difference to the lives of vulnerable people.</p>
  </div>
  <p class="lead-in" style="left:19px;top:258px">We have a comprehensive database of the following personnel</p>
  <ul class="bullets" style="left:19px;top:276px;width:160px">
    <li>Registered Nurses (Aged Care, Disability, Emergency, Public and Private healthcare)</li>
    <li>Clinical Nurses</li>
    <li>Nurse Practitioners</li>
    <li>Enrolled Nurses</li>
    <li>Assistants in Nursing (Carers/ PCA’s)</li>
    <li>Support Workers (Disability, Community</li>
    <li>and Mental health)</li>
    <li>Healthcare Endorsed Chefs and Cooks</li>
    <li>Catering Assistants</li>
    <li>Kitchen hands</li>
    <li>Cleaner</li>
  </ul>
  <div class="brand brand--purple" style="left:40px;top:476px;font-size:13px"><span class="brand__dot"></span>Calm Fern Wellcare</div>
  <p class="url-foot" style="right:22px;top:518px">www.calmfernwellcare.com.au</p>
</section>

<!-- Contact -->
<section class="page page--contact">
  <div class="photo" role="img" aria-label="Elderly woman laughing with a younger woman while doing a jigsaw puzzle at a table" style="left:0;top:0;width:386px;height:420px;background:linear-gradient(150deg,#e9e6e2,#d8c2b4 40%,#a97f88 65%,#efe6da)"></div>
  <svg class="waves" viewBox="0 0 386 542" aria-hidden="true">
    <defs>
      <linearGradient id="g4" x1="0" x2="1"><stop offset="0" stop-color="#6b449b"/><stop offset="1" stop-color="#886aae"/></linearGradient>
    </defs>
    <path d="M0 385C100 350 220 375 300 380C340 382 366 372 386 360V420H0Z" fill="#eea4c8"/>
    <path d="M0 395C100 362 220 388 300 392C340 394 366 384 386 374V420H0Z" fill="#fff"/>
    <path d="M0 405C100 372 220 398 300 402C340 404 366 394 386 384V542H0Z" fill="url(#g4)"/>
  </svg>
  <div class="brand" style="left:40px;top:470px;font-size:13px"><span class="brand__dot"></span>Calm Fern Wellcare</div>
  <div class="contact">
    <div class="contact__title">Contact Us</div>
    <div class="contact__row contact__row--phone">
      <svg width="9" height="11" viewBox="0 0 10 12" aria-hidden="true"><path d="M2 1h2l1 3-1.5 1a6 6 0 0 0 3 3L7.5 6.5l3 1V10c0 1-1 1.5-2 1.2A10 10 0 0 1 1 3C.8 2 1 1 2 1Z" fill="#eea4c8"/></svg>
      08 5550 1234
    </div>
    <div class="contact__row">
      <svg width="7" height="9" viewBox="0 0 8 10" aria-hidden="true"><path d="M4 0a3.5 3.5 0 0 1 3.5 3.5C7.5 6 4 10 4 10S.5 6 .5 3.5A3.5 3.5 0 0 1 4 0Z" fill="#eea4c8"/><circle cx="4" cy="3.5" r="1.3" fill="#6b449b"/></svg>
      14 Wattle Lane, Easton WA 6000
    </div>
    <div class="contact__row">
      <svg width="8" height="6" viewBox="0 0 8 6" aria-hidden="true"><rect width="8" height="6" rx="1" fill="#eea4c8"/><path d="M0 .5 4 3.5 8 .5" stroke="#6b449b" stroke-width=".8" fill="none"/></svg>
      admin@calmfernwellcare.com.au
    </div>
    <div class="contact__row">
      <svg width="8" height="8" viewBox="0 0 8 8" aria-hidden="true"><circle cx="4" cy="4" r="3.5" fill="none" stroke="#eea4c8" stroke-width=".9"/><path d="M.5 4h7M4 .5c-2 2-2 5 0 7M4 .5c2 2 2 5 0 7" stroke="#eea4c8" stroke-width=".7" fill="none"/></svg>
      www.calmfernwellcare.com.au
    </div>
  </div>
</section>

</body>
</html>
```